Homepage Redesign for Healthcare Tech Company

This is for a redesign of our current homepage. We have specific notes and a Mockup and we need a great designer to bring it to life and make it look sophisticated and professional. Please see the Current Page (attached and online) as well as the Notes doc and Mockup PPT, both attached, for what we need.

Overall, look at the current page as a sketch of what it could be. We would like a design that really nails the structure of both the overall page and the pipeline (that runs through Sections 1-4), so that it looks like one, clean, custom design (not pieced together). It’s important that the basic structure of the pipeline, especially the transition from icons to screenshots (starting in section 2, and mostly in section 3) all flow together well and look like a deliberate, well thought-out design. Please include that, and at least the headlines for each section, in any initial submissions.

We will be building out of website beyond just this page, and would be great to work with a designer we can continue working with on the website, the graphical screenshots and some infographics. Not a must but definitely an option if you would like. We didn’t include all pages in this project, because we would like the designer to focus all energy on creating a well thought-out homepage design with the wow factor, and we can build it out together from there. For now, we would like just 2 additional general theme pages (one smaller page for a couple paragraphs of text only and one with a few uniform sections, with room for text and small graphic-see notes).

Our customers are healthcare companies – both Doctors and IT professionals of medium to large healthcare organizations who support doctors. We are experts in healthcare interoperability technology and the page should reflect that. Medical Record documentation is an expensive time-consuming massive headache for our customer base. What we are offering is a truly groundbreaking solution that leverages the best technology available to bring them something that wasn’t possible before – ALL of their patient data in one enriched and linked document, delivered to their current workflow. It's an expensive solution but very impactful in terms of better patient care and dramatically streamlined workflow - the homepage needs to reflect that. Please take the time to understand the solution we offer and just let me know if you need clarification – I’m happy to answer any questions.

Thanks!

SEE ATTACHMENTS, and also this more detailed breakdown of the sections: https://qv.fx/Tr4mPz

Target Market(s)

Doctors, IT Professionals in the Healthcare field, Medical Coders..but focus should be on Doctors

Number of Pages Required

1 page

Colors
0355a3
3276b5
0293ce
6b449b
886aae
b7a5cd
00a990
33b8a4
86cfc6

Requirements
Must have
• - Sophisticated, professional, masterful layout
- Must refer to the attached DESIGN NOTES.doc (about 2 pages) and MOCKUP.PPT but bring the idea to life in an innovative way. In general, we collect all medical records, summarize and unify into 1 document that we send straight into each patient file, but referring to the actual notes to truly get what we do and what we need it is a must.
- Framing/background emphasis for provided screenshots (even if these screenshots don't fit exactly, we will make them fit after)
- Emphasis on the fact that clicking the View Source buttons in the Lumora (what we call our product) opens the actual source documents (underlying medical record) - this is a big deal for doctors and medical coders.
- Final design should be in editable PSD file
Nice to have
• Animation. We are asking for design only because we want the best design possible but we would definitely choose a great animated design (assuming that means you'd need to code it too - let me know) and ensure that you are paid the extra for coding if you need to code it yourself.
Should not have
• template feel - should look custom
cheesy photos of models dressed as doctors

```html
<!DOCTYPE html>
<html lang="en">
<head>
<meta charset="utf-8">
<title>Clarevo — Unified Patient Intelligence</title>
<link rel="stylesheet" href="https://fonts.googleapis.com/css2?family=Poppins:wght@300;400;500;600;700;800&display=swap">
<style>
:root{
  --ink:#050508;
  --navy:#141633;
  --navy-2:#1c1d44;
  --purple:#6b449b;
  --lilac:#886aae;
  --lavender:#b7a5cd;
  --blue:#0355a3;
  --blue-2:#3276b5;
  --sky:#0293ce;
  --teal:#00a990;
  --teal-2:#33b8a4;
  --mint:#86cfc6;
  --glow:#35e6dc;
  --text:#ffffff;
  --muted:#b9bccb;
  --card:rgba(120,110,150,.28);
}
*{margin:0;padding:0;box-sizing:border-box}
html,body{width:1200px;height:4986px;overflow:hidden;background:var(--ink)}
body{font-family:"Poppins",sans-serif;color:var(--text);position:relative}
.section{position:relative;width:1200px;overflow:hidden}
.abs{position:absolute}
h1,h2,h3,h4{font-weight:700;letter-spacing:.2px}
.card{position:absolute;background:var(--card);border-radius:14px}
.card h2{font-size:24px;line-height:1.2;text-transform:uppercase;font-weight:800}
.card p{font-size:13px;line-height:1.6;color:var(--muted);margin-top:14px}
.btn{display:inline-block;background:linear-gradient(90deg,var(--purple),var(--teal-2));color:#fff;font-size:13px;font-weight:500;border-radius:4px;text-decoration:none;text-align:center}
.pipeline{position:absolute;left:599px;width:2px;background:linear-gradient(180deg,rgba(53,230,220,0),var(--glow) 3%,var(--glow) 97%,rgba(53,230,220,0));box-shadow:0 0 8px var(--glow);z-index:1}
.dot{position:absolute;width:10px;height:10px;border-radius:50%;background:var(--glow);box-shadow:0 0 10px 3px rgba(53,230,220,.7);z-index:2}
.shot{position:absolute;border-radius:10px;background:linear-gradient(180deg,#f4f6fa,#dfe4ee);box-shadow:0 10px 40px rgba(0,0,0,.5);z-index:3}
.doc{position:absolute;background:linear-gradient(180deg,#fbfbfd,#e6e9f0);border:3px solid var(--purple);z-index:3}

.nav{position:absolute;top:0;left:0;width:1200px;height:78px;border-bottom:1px solid rgba(255,255,255,.12);z-index:5}
.brand{position:absolute;left:74px;top:26px;display:flex;align-items:center;gap:10px;font-size:22px;font-weight:600;letter-spacing:.5px}
.brand i{width:24px;height:24px;background:var(--teal-2);display:block}
.nav ul{position:absolute;left:330px;top:30px;display:flex;gap:26px;list-style:none;font-size:12px;font-weight:500}
.nav .btn{position:absolute;right:72px;top:22px;width:122px;height:32px;line-height:32px;font-size:12px}

.hero{height:673px;background:radial-gradient(ellipse at 70% 40%,#1c1a2c,var(--ink) 60%)}
.hero h1{position:absolute;left:74px;top:160px;font-size:42px;line-height:1.2;font-weight:800}
.hero .lede{position:absolute;left:74px;top:275px;width:400px;color:var(--teal-2);font-size:21px;font-weight:700;line-height:1.25}
.hero .intro{position:absolute;left:74px;top:372px;width:400px;font-size:13px;line-height:1.6}
.hero .btn{position:absolute;left:74px;top:522px;width:162px;height:46px;line-height:46px}
.hero-art{position:absolute;left:520px;top:60px;width:560px;height:560px;border-radius:50%;background:radial-gradient(circle,rgba(107,68,155,.55),rgba(0,169,144,.25) 45%,rgba(5,5,8,0) 70%)}

.network{height:1117px;background:linear-gradient(100deg,#121430 0%,#1a1b42 45%,#2a2050 100%)}
.network .center-glow{position:absolute;left:350px;top:300px;width:500px;height:820px;background:radial-gradient(ellipse,rgba(90,90,170,.35),rgba(0,0,0,0) 65%)}
.network h3.title{position:absolute;left:0;width:1200px;top:280px;text-align:center;font-size:27px;font-weight:800}
.node-text{position:absolute;width:240px}
.node-text h4{font-size:16px;font-weight:700}
.node-text p{font-size:13px;line-height:1.6;color:var(--muted);margin-top:12px}
.node{position:absolute;width:70px;height:70px;border-radius:50%;border:2px solid var(--lilac);background:rgba(107,68,155,.25);display:flex;align-items:center;justify-content:center;z-index:2}
.node .core{width:50px;height:50px;border-radius:50%;background:linear-gradient(135deg,var(--blue-2),var(--purple));display:flex;align-items:center;justify-content:center}

.transform{height:675px;background:radial-gradient(ellipse at 50% 60%,#1d1f40,var(--ink) 55%)}
.hub{position:absolute;left:540px;top:71px;width:120px;height:120px;border-radius:50%;background:radial-gradient(circle,#1a5560,#0b2530 60%);border:3px solid rgba(53,230,220,.35);box-shadow:0 0 40px rgba(53,230,220,.45);z-index:2;display:flex;align-items:center;justify-content:center}
.hub span{width:44px;height:44px;border-radius:50%;border:2px solid var(--glow)}
.note{font-size:14px;line-height:1.55;color:var(--muted)}

.insights{height:890px;background:linear-gradient(120deg,#10323a 0%,#0f2533 45%,#1a1a3c 100%)}
.feature-label h4{font-size:17px}
.feature-label p{font-size:13px;line-height:1.6;color:var(--muted);margin-top:10px}
.source-btn{position:absolute;width:64px;height:22px;border-radius:3px;background:var(--lilac);font-size:10px;font-weight:600;line-height:22px;text-align:center;z-index:4}

.ehr{height:557px;background:var(--ink)}
.vendors{display:grid;grid-template-columns:repeat(3,1fr);row-gap:22px;column-gap:8px;margin-top:22px}
.vendors span{font-size:16px;font-weight:600;white-space:nowrap}

.benefits{height:362px;background:linear-gradient(100deg,#0f3236,#141a3e)}
.benefit{position:absolute;top:107px;width:250px}
.benefit .icon{width:36px;height:36px;border-radius:50%;border:2px solid var(--teal-2);display:flex;align-items:center;justify-content:center}
.benefit .icon b{width:12px;height:12px;border-radius:50%;background:#fff}
.benefit h4{margin-top:27px;font-size:16px;font-weight:700}
.benefit p{margin-top:14px;font-size:13px;line-height:1.6;color:var(--muted)}
.benefit + .benefit{border-left:1px solid rgba(255,255,255,.12)}

.news{height:401px;background:linear-gradient(100deg,#161835,#1f1d40)}
.news h2{position:absolute;left:74px;top:68px;font-size:20px;font-weight:800}
.news .card{left:194px;top:95px;width:812px;height:223px;background:rgba(120,110,160,.2)}
.story{position:absolute;top:50px;width:210px;height:140px}
.story time{font-size:11px;color:var(--muted)}
.story h5{margin-top:14px;font-size:13px;font-weight:500;line-height:1.5}
.story a{position:absolute;top:120px;left:0;font-size:11px;font-weight:600;color:var(--purple);text-decoration:none}

.footer{height:311px;background:linear-gradient(180deg,#141a3a,#0e1430)}
.footer .mark{position:absolute;left:222px;top:70px;width:50px;height:50px;background:var(--teal-2)}
.footer p{position:absolute;left:358px;width:600px;font-size:12px;line-height:1.75;color:var(--muted)}
</style>
</head>
<body>

<header class="nav">
  <div class="brand"><i></i>CLAREVO</div>
  <ul><li>About</li><li>Features</li><li>Features</li><li>Process</li><li>Team</li><li>Clients</li></ul>
  <a class="btn" href="#">Request Access</a>
</header>

<section class="section hero">
  <div class="hero-art" role="img" aria-label="Abstract particle burst illustration in purple and teal"></div>
  <h1>UNIFIED PATIENT<br>INTELLIGENCE</h1>
  <p class="lede">Each patients' full medical history, summary and analysis in one comprehensive health record</p>
  <p class="intro">Clarevo collects patients' records from all sources of external clinical data, synthesizes the captured data into one composite health record, abstracts all HCC, MIPS and HEDIS opportunities, and delivers them directly into your EHR, all in a matter of hours.</p>
  <a class="btn" href="#">Request Access</a>
</section>

<section class="section network">
  <div class="center-glow"></div>
  <div class="card" style="left:48px;top:39px;width:484px;height:210px;padding:48px 26px">
    <h2>Your patients' full medical<br>history from all sources</h2>
    <p>Clarevo clinical data network has unprecedented<br>reach across the continuum of care.</p>
  </div>
  <h3 class="title">CLAREVO CLINICAL DATA NETWORK</h3>

  <div class="pipeline" style="top:400px;height:717px"></div>
  <svg class="abs" style="left:0;top:0;z-index:1" width="1200" height="1117" fill="none" stroke="#35e6dc" stroke-width="2">
    <path d="M466 415 C560 415 600 440 600 500"/><path d="M734 415 C640 415 600 440 600 500"/>
    <path d="M466 635 C560 635 600 660 600 720"/><path d="M734 635 C640 635 600 660 600 720"/>
    <path d="M466 855 C560 855 600 880 600 940"/><path d="M734 855 C640 855 600 880 600 940"/>
  </svg>
  <div class="dot" style="left:478px;top:410px"></div><div class="dot" style="left:712px;top:410px"></div>
  <div class="dot" style="left:478px;top:630px"></div><div class="dot" style="left:712px;top:630px"></div>
  <div class="dot" style="left:478px;top:850px"></div><div class="dot" style="left:712px;top:850px"></div>

  <div class="node" style="left:395px;top:380px"><div class="core"><svg width="22" height="22" viewBox="0 0 24 24" fill="none" stroke="#fff" stroke-width="2"><rect x="3" y="4" width="18" height="12"/><path d="M8 20h8M12 16v4"/></svg></div></div>
  <div class="node" style="left:735px;top:380px"><div class="core"><svg width="22" height="22" viewBox="0 0 24 24" fill="none" stroke="#fff" stroke-width="2"><path d="M6 3h8l4 4v14H6z"/><path d="M9 10v7M9 10h3a2 2 0 010 4H9M12 14l3 3"/></svg></div></div>
  <div class="node" style="left:395px;top:600px"><div class="core"><svg width="22" height="22" viewBox="0 0 24 24" fill="none" stroke="#fff" stroke-width="2"><path d="M15 3l6 6L9 21H3v-6z"/></svg></div></div>
  <div class="node" style="left:735px;top:600px"><div class="core"><svg width="22" height="22" viewBox="0 0 24 24" fill="none" stroke="#fff" stroke-width="2"><path d="M4 8h15l-4-4M20 16H5l4 4"/></svg></div></div>
  <div class="node" style="left:395px;top:820px"><div class="core"><svg width="22" height="22" viewBox="0 0 24 24" fill="none" stroke="#fff" stroke-width="2"><path d="M4 21V8h6V3h10v18z"/><path d="M13 8h4M13 12h4M13 16h4M7 12h1M7 16h1"/></svg></div></div>
  <div class="node" style="left:735px;top:820px"><div class="core"><svg width="22" height="22" viewBox="0 0 24 24" fill="none" stroke="#fff" stroke-width="2"><path d="M12 3l8 3v6c0 5-4 8-8 9-4-1-8-4-8-9V6z"/><path d="M8 12l3 3 5-5"/></svg></div></div>

  <div class="node-text" style="left:74px;top:390px"><h4>EMR Networks</h4><p>Connected to 800,000 Physician EMR databases and over 60,000 hospitals across the country.</p></div>
  <div class="node-text" style="left:74px;top:610px"><h4>Diagnostic Labs</h4><p>Clarevo is directly connected to all major diagnostic testing laboratories, enabling collection of all lab results.</p></div>
  <div class="node-text" style="left:74px;top:830px"><h4>Provider Faxes</h4><p>Fax records received from PCPs and specialists are converted into structured, searchable electronic records (C-CD) for ingestion into the Clarevo Lumora℠.</p></div>
  <div class="node-text" style="left:876px;top:390px;width:250px"><h4>RX Data or US Pharmacies</h4><p>Comprehensive medication history including medication starts, adherence, and switching behavior is collected from national and regional pharmacy data feeds. This includes specialized pharmacies.</p></div>
  <div class="node-text" style="left:876px;top:610px;width:250px"><h4>HIE Networks</h4><p>Aggregating from 32 Health Information Exchange networks for real-time access to clinical data.</p></div>
  <div class="node-text" style="left:876px;top:830px;width:250px"><h4>Claims Databases</h4><p>Connected to the nation's largest clearing houses for open and closed claims submission and processing, including Medicare Part A, B and D data for 53 million Medicare beneficiaries. This includes Medical &amp; Rx Open/Closed Claims EDI and Remittance ERI.</p></div>
</section>

<section class="section transform">
  <div class="pipeline" style="top:0;height:675px"></div>
  <div class="card" style="left:48px;top:40px;width:436px;height:230px;padding:28px 26px">
    <h2 style="font-size:19px">Transformed into 1 composite<br>C-CDA heath record</h2>
    <p>The Clarevo synthesis engine utilizes OCR, advanced parsing techniques, Clinical Natural Language Processing (cNLP), proprietary logic and NPI matching to clean, de-duplicate, structure and enrich all inputs from data acquisition.</p>
  </div>
  <div class="hub"><span></span></div>
  <div class="card" style="left:722px;top:303px;width:330px;height:225px;padding:38px 40px 0 82px;background:rgba(110,105,140,.3)">
    <p class="note" style="margin:0;font-size:13px">The normalized data is unified into the Lumora C-CDA, an enhanced composite longitudinal record in C-CDA format, the industry standard for all interoperability initiatives</p>
  </div>
  <div class="shot" style="left:434px;top:338px;width:334px;height:216px;border:3px solid #fff" role="img" aria-label="Screenshot of the Lumora C-CDA record with insurance, medications, results and problems tables"></div>
  <div class="dot" style="left:595px;top:600px"></div>
</section>

<section class="section insights">
  <div class="pipeline" style="top:0;height:890px"></div>
  <div class="card" style="left:48px;top:65px;width:510px;height:190px;padding:30px 26px">
    <h2 style="font-size:19px">Summarized and linked &nbsp;to key insights</h2>
    <p>Insights are presented in a concise summary with direct links to supporting evidence. HCC, HEDIS and MIPS opportunities are abstracted and cross-linked directly to the original text in the underlying record for quick and easy reference.</p>
  </div>
  <div class="feature-label abs" style="left:74px;top:323px;width:200px"><h4>Risk-Adjustment</h4><p>HCC opportunities for new capture and recapture are identified and extracted using logic algorithms.</p></div>
  <div class="feature-label abs" style="left:74px;top:470px;width:200px"><h4>Quality Analysis</h4><p>HEDIS and MIPS quality measure gaps closed using NQAB certified technology to generate QRDAIII.</p></div>

  <div class="card" style="left:768px;top:109px;width:384px;height:677px;background:rgba(110,105,140,.28)"></div>
  <svg class="abs" style="left:0;top:0;z-index:3" width="1200" height="890" fill="none" stroke="#35e6dc" stroke-width="1.5">
    <path d="M870 410 H915 V302"/><path d="M870 464 H945"/><path d="M870 516 H915 V608"/>
  </svg>
  <div class="doc" style="left:813px;top:176px;width:205px;height:126px" role="img" aria-label="Source document: scanned clinical note"></div>
  <div class="doc" style="left:945px;top:395px;width:205px;height:130px;border-color:var(--teal)" role="img" aria-label="Source document: lab results report"></div>
  <div class="doc" style="left:813px;top:608px;width:205px;height:129px" role="img" aria-label="Source document: medication table"></div>

  <div class="shot" style="left:306px;top:321px;width:334px;height:281px;background:linear-gradient(180deg,#c9cdd8,#aeb4c2);opacity:.7" role="img" aria-label="Background screenshot of the Lumora record"></div>
  <div class="shot" style="left:316px;top:370px;width:318px;height:226px;border:2px solid #fff" role="img" aria-label="Screenshot of the Lumora summary listing HCC and quality opportunities"></div>
  <div class="shot" style="left:662px;top:354px;width:138px;height:180px;background:linear-gradient(180deg,#fff,#eceef4)" role="img" aria-label="Insight detail popup with linked evidence"></div>
  <div class="source-btn" style="left:806px;top:399px">View Source</div>
  <div class="source-btn" style="left:806px;top:453px;background:var(--teal-2)">View Source</div>
  <div class="source-btn" style="left:806px;top:505px;background:var(--blue-2)">View Source</div>
</section>

<section class="section ehr">
  <div class="pipeline" style="top:0;height:260px"></div>
  <div class="card" style="left:48px;top:75px;width:402px;height:120px;padding:30px 26px">
    <h2 style="font-size:19px">Delivered directly into your<br>EHR for native viewing</h2>
  </div>
  <p class="note abs" style="left:240px;top:236px;width:140px;font-size:13px">The final package is delivered as a single longitudinal record into each patient's chart within your EHR, viewable natively</p>
  <div class="card" style="left:714px;top:175px;width:414px;height:297px;padding:40px 26px 0 84px;background:rgba(110,105,140,.3)">
    <p class="note" style="font-size:13px">The Clarevo Lumora is compatible with any Meaningful Use certified EHR.</p>
    <div class="vendors">
      <span style="color:var(--teal)">Medarix</span><span style="color:#e0a066">Velquon</span><span>Quintara</span>
      <span style="color:var(--lavender)">Nuvelline</span><span style="color:#e04a4a">Zephra</span><span style="color:var(--sky)">Corvexa</span>
      <span style="color:var(--teal-2)">Praxilo</span><span style="color:var(--blue-2)">Tessaro</span>
    </div>
  </div>
  <div class="dot" style="left:595px;top:212px"></div>
  <div class="shot" style="left:450px;top:225px;width:316px;height:183px;background:linear-gradient(180deg,#e8edf5,#c7d2e4)" role="img" aria-label="Screenshot of the Lumora record displayed inside an EHR patient chart"></div>
</section>

<section class="section benefits">
  <div class="benefit" style="left:74px;padding-right:20px"><div class="icon"><b></b></div><h4>1-CLICK ACCESS</h4><p>1-click access to each inference and insight in the underlying record</p></div>
  <div class="benefit" style="left:300px;padding-left:20px"><div class="icon"><b></b></div><h4>SEARCHABLE</h4><p>All data in the Lumora CCDA is searchable, including previously unstructured data</p></div>
  <div class="benefit" style="left:577px;padding-left:20px"><div class="icon"><b></b></div><h4>SEAMLESS INTEGRATION</h4><p>Designed for seamless integration into your current tools and workflow</p></div>
  <div class="benefit" style="left:852px;padding-left:20px"><div class="icon"><b></b></div><h4>EMPOWER PHYSICIANS</h4><p>Provide physicians with a complete summarized medical history linked to supporting documentation ahead of every encounter</p></div>
</section>

<section class="section news">
  <h2>NEWS</h2>
  <div class="card">
    <article class="story" style="left:60px"><time>March 5, 2020</time><h5>Quorvane wins first major Harbor Care deal as Stellix is passed over.</h5><a href="#">Read More</a></article>
    <article class="story" style="left:308px"><time>February 26, 2020</time><h5>Tomas Rendle: When is shared data not in the patient's interest?</h5><a href="#">Read More</a></article>
    <article class="story" style="left:556px"><time>December 14, 2019</time><h5>Quorvane Wins New Velmont Health Deal With $11 Million Award</h5><a href="#">Read More</a></article>
  </div>
</section>

<footer class="section footer">
  <div class="mark"></div>
  <p style="top:45px">The Clarevo Lumora is a game-changing tool designed to accelerate success in value-based contracts by maximizing outcomes, scores and revenue while significantly decreasing inefficiencies and administrative burden.</p>
  <p style="top:130px">Clarevo platform has been shaped by our partnerships with the leaders in value-based care to address their most complex challenges. We are experts in interoperability technology and are passionate about empowering healthcare organizations to achieve market-leading results.</p>
  <p style="top:245px;font-size:11px">© Copyright CLAREVO 2020 | All Rights Reserved.</p>
</footer>

</body>
</html>
```